Tellborne Medical

Need smart and sleek business cards design for my medical distribution company. use logos attached.

add my details

Lorcan Pettifer
Director/Sales Agent
lorcan@tellbornemedical-example.com.au
0491 638 170

```html
<!DOCTYPE html>
<html lang="en">
<head>
<meta charset="utf-8">
<title>Tellborne Medical – Business Cards</title>
<link rel="stylesheet" href="https://fonts.googleapis.com/css2?family=Poppins:wght@400;500;700&display=swap">
<style>
  :root {
    --navy: #1b2559;
    --navy-deep: #16204d;
    --blue: #2a86c4;
    --ink: #1f2a5c;
    --grey-text: #4a4f5e;
    --card-light: #f3f4f7;
    --card-shade: #dcdee5;
    --rule: #3a3f6e;
    --stage: #e9e9ec;
  }
  * { box-sizing: border-box; margin: 0; padding: 0; }
  html, body {
    width: 1200px;
    height: 900px;
    overflow: hidden;
    background: var(--stage);
    font-family: "Poppins", sans-serif;
  }
  .canvas {
    width: 1200px;
    height: 900px;
    display: flex;
    flex-direction: column;
    align-items: center;
    justify-content: center;
    gap: 44px;
  }
  .card {
    width: 640px;
    height: 391px;
    border-radius: 34px;
    position: relative;
    overflow: hidden;
    box-shadow: 0 14px 30px rgba(20, 25, 50, 0.22);
  }
  .card--back {
    background: radial-gradient(ellipse at 65% 40%, var(--navy) 0%, var(--navy-deep) 80%);
    display: flex;
    align-items: center;
    justify-content: center;
  }
  .brand {
    display: flex;
    align-items: center;
    gap: 14px;
    font-weight: 700;
    letter-spacing: 0.04em;
    text-transform: uppercase;
  }
  .brand__mark {
    width: 22px;
    height: 22px;
  }
  .brand--light { color: #ffffff; font-size: 40px; }
  .brand--light .brand__mark { background: #ffffff; }
  .brand--dark { color: var(--navy); font-size: 32px; }
  .brand--dark .brand__mark { background: var(--navy); }

  .card--front {
    background: linear-gradient(135deg, var(--card-shade) 0%, var(--card-light) 55%, #ffffff 100%);
    padding: 58px 0 0;
  }
  .card--front .brand {
    justify-content: center;
  }
  .identity {
    position: relative;
    margin-top: 54px;
    text-align: center;
  }
  .identity__rule {
    position: absolute;
    top: 50%;
    height: 1px;
    background: var(--rule);
  }
  .identity__rule--left { left: 0; width: 190px; }
  .identity__rule--right { right: 0; width: 190px; }
  .identity__name {
    font-weight: 700;
    font-size: 22px;
    color: var(--navy);
    text-transform: uppercase;
    letter-spacing: 0.01em;
  }
  .identity__title {
    font-size: 17px;
    color: var(--grey-text);
  }
  .contacts {
    margin-top: 26px;
    display: flex;
    flex-direction: column;
    align-items: center;
    gap: 12px;
    font-size: 17px;
    color: var(--ink);
  }
  .contacts__item {
    display: flex;
    align-items: center;
    gap: 9px;
  }
  .contacts__icon {
    width: 17px;
    height: 17px;
    fill: var(--blue);
    flex: none;
  }
</style>
</head>
<body>
<main class="canvas">
  <section class="card card--back" aria-label="Card back">
    <div class="brand brand--light">
      <span class="brand__mark"></span>
      <span class="brand__name">Tellborne Medical</span>
    </div>
  </section>

  <section class="card card--front" aria-label="Card front">
    <div class="brand brand--dark">
      <span class="brand__mark"></span>
      <span class="brand__name">Tellborne Medical</span>
    </div>

    <div class="identity">
      <span class="identity__rule identity__rule--left"></span>
      <span class="identity__rule identity__rule--right"></span>
      <p class="identity__name">Lorcan Pettifer</p>
      <p class="identity__title">Director/Sales Agent</p>
    </div>

    <div class="contacts">
      <p class="contacts__item">
        <svg class="contacts__icon" viewBox="0 0 24 24" aria-hidden="true">
          <path d="M6.6 10.8c1.4 2.8 3.8 5.1 6.6 6.6l2.2-2.2c.3-.3.7-.4 1-.2 1.1.4 2.3.6 3.6.6.6 0 1 .4 1 1V20c0 .6-.4 1-1 1C10.6 21 3 13.4 3 4c0-.6.4-1 1-1h3.5c.6 0 1 .4 1 1 0 1.3.2 2.5.6 3.6.1.3 0 .7-.2 1L6.6 10.8z"/>
        </svg>
        <span>0491 638 170</span>
      </p>
      <p class="contacts__item">
        <svg class="contacts__icon" viewBox="0 0 24 24" aria-hidden="true">
          <path d="M3 5h18c.6 0 1 .4 1 1v12c0 .6-.4 1-1 1H3c-.6 0-1-.4-1-1V6c0-.6.4-1 1-1zm1 2.2V17h16V7.2l-8 5.3-8-5.3zM5.6 7 12 11.2 18.4 7H5.6z"/>
        </svg>
        <span>lorcan@tellbornemedical-example.com.au</span>
      </p>
    </div>
  </section>
</main>
</body>
</html>
```